Half-fold brochure for Birch Glow & Laser membership

We would like a professional designer to help us with designing a half-fold brochure for our membership program. Attached to this project is the draft brochure to showcase the content and typical color scheme. Please take a moment to visit oue website and Instagram to get an idea of what our brand is about.

www.BirchGlowLaser.example
www.Instagram.com/BirchGlowLaser

Target Market(s)

25 - 45 female working professional

Industry/Entity Type

Beauty

Font styles to use
Other font styles liked:
• Josefin Sans, Lato

Colors

Designer to choose colors to be used in the design.

Requirements
Must have
• Logo, color scheme, website, instagram address, facebook address, pictures
Nice to have
• Mobile app mock-up
Should not have
• models outside of 25 - 45 age range

```html
<!DOCTYPE html>
<html lang="en">
<head>
<meta charset="UTF-8">
<title>Birch Glow & Laser — Membership Brochure Spread</title>
<link rel="stylesheet" href="https://fonts.googleapis.com/css2?family=Josefin+Sans:wght@400;600;700&family=Lato:wght@300;400;700;900&display=swap">
<style>
  :root {
    --amber: #f0ae3c;
    --ink: #1d1d1d;
    --text: #2a2a2a;
    --muted: #8a8a8a;
    --paper: #f7f7f6;
    --paper-edge: #ececeb;
    --backdrop: #d4d3d3;
  }
  * { box-sizing: border-box; margin: 0; padding: 0; }
  html, body {
    width: 1200px; height: 900px; overflow: hidden;
    background: var(--backdrop);
    font-family: "Lato", sans-serif;
    color: var(--text);
  }
  .spread {
    position: absolute; left: 60px; top: 70px;
    width: 1080px; height: 760px;
    display: flex;
    box-shadow: 0 20px 50px rgba(0,0,0,0.18);
  }
  .page {
    position: relative; width: 540px; height: 760px;
    background: var(--paper); overflow: hidden;
  }
  .page--left { border-right: 1px solid var(--paper-edge); }

  .brand {
    position: absolute; left: 48px; top: 46px;
    display: flex; align-items: center; gap: 8px;
    font-family: "Lato", sans-serif; font-weight: 900;
    font-size: 15px; color: var(--ink);
  }
  .brand__dot { width: 14px; height: 14px; border-radius: 50%; background: var(--amber); }

  .page__title {
    font-family: "Josefin Sans", sans-serif; font-weight: 700;
    color: var(--ink); line-height: 1;
  }
  .page__lead { font-weight: 900; font-size: 16px; color: var(--ink); margin-top: 8px; }

  /* Rewards page */
  .rewards { position: absolute; left: 48px; top: 96px; right: 40px; }
  .rewards .page__title { font-size: 40px; }
  .rewards__note {
    font-weight: 300; font-size: 15px; color: var(--muted);
    margin: 22px 0 12px;
  }
  .voucher-row { display: flex; gap: 14px; }
  .voucher {
    width: 140px; height: 66px; display: flex;
    clip-path: polygon(0 0, 100% 0, 96% 12%, 100% 25%, 96% 37%, 100% 50%, 96% 62%, 100% 75%, 96% 87%, 100% 100%, 0 100%, 4% 87%, 0 75%, 4% 62%, 0 50%, 4% 37%, 0 25%, 4% 12%);
  }
  .voucher__stub {
    width: 34px; background: var(--amber);
    display: flex; align-items: center; justify-content: center;
  }
  .voucher__stub span {
    transform: rotate(90deg); white-space: nowrap;
    font-size: 9px; font-weight: 700; letter-spacing: 1px; color: #fff;
  }
  .voucher__body {
    flex: 1; background: var(--ink); color: #fff;
    display: flex; flex-direction: column; align-items: center; justify-content: center;
    padding-right: 4px;
  }
  .voucher__tag { font-size: 8px; font-weight: 700; letter-spacing: .5px; }
  .voucher__value { font-family: "Lato", sans-serif; font-weight: 900; font-size: 26px; line-height: 1.05; }
  .voucher__service { font-weight: 300; font-size: 12px; line-height: 1.1; text-align: center; margin-top: 3px; }

  .rewards__photo {
    position: absolute; left: 0; right: 0; bottom: 0; height: 300px;
    background: linear-gradient(160deg, #e7e6e4 0%, #cfcdcb 45%, #d9c4bd 70%, #efeeed 100%);
  }

  /* Perks page */
  .perks { position: absolute; left: 48px; top: 96px; right: 40px; }
  .perks .page__title { font-size: 44px; }
  .perks__list { list-style: none; margin-top: 16px; }
  .perks__list li { font-size: 16px; line-height: 1.5; color: var(--text); }

  .perks__visual { position: absolute; left: 70px; top: 300px; width: 500px; height: 480px; }
  .perks__photo {
    position: absolute; left: 70px; top: 50px; width: 400px; height: 400px;
    border-radius: 50%;
    background: radial-gradient(circle at 45% 50%, #f2d3b5 0%, #e7c08f 30%, #f3f1ee 60%, #e2e0dd 100%);
  }
</style>
</head>
<body>
<main class="spread">
  <section class="page page--left">
    <div class="brand"><span class="brand__dot"></span>Birch Glow &amp; Laser</div>
    <div class="rewards">
      <h1 class="page__title">Glowpoint Rewards</h1>
      <p class="page__lead">All members earn 1 point per $1 spent.</p>

      <p class="rewards__note">Redeem points for vouchers.</p>
      <div class="voucher-row">
        <div class="voucher"><div class="voucher__stub"><span>VOUCHER</span></div><div class="voucher__body"><span class="voucher__tag">★ VOUCHER ★</span><span class="voucher__value">$5</span></div></div>
        <div class="voucher"><div class="voucher__stub"><span>VOUCHER</span></div><div class="voucher__body"><span class="voucher__tag">★ VOUCHER ★</span><span class="voucher__value">$10</span></div></div>
        <div class="voucher"><div class="voucher__stub"><span>VOUCHER</span></div><div class="voucher__body"><span class="voucher__tag">★ VOUCHER ★</span><span class="voucher__value">$15</span></div></div>
      </div>

      <p class="rewards__note">Redeem points for vouchers.</p>
      <div class="voucher-row">
        <div class="voucher"><div class="voucher__stub"><span>VOUCHER</span></div><div class="voucher__body"><span class="voucher__tag">★ VOUCHER ★</span><span class="voucher__service">Laser Hair<br>Removal</span></div></div>
        <div class="voucher"><div class="voucher__stub"><span>VOUCHER</span></div><div class="voucher__body"><span class="voucher__tag">★ VOUCHER ★</span><span class="voucher__service">IPL Facial</span></div></div>
        <div class="voucher"><div class="voucher__stub"><span>VOUCHER</span></div><div class="voucher__body"><span class="voucher__tag">★ VOUCHER ★</span><span class="voucher__service">Chemical<br>Peel</span></div></div>
      </div>
    </div>
    <div class="rewards__photo" role="img" aria-label="Photo of a client receiving a facial skin treatment from a gloved therapist"></div>
  </section>

  <section class="page page--right">
    <div class="brand"><span class="brand__dot"></span>Birch Glow &amp; Laser</div>
    <div class="perks">
      <h2 class="page__title">Other Perks</h2>
      <p class="page__lead">Continue benefiting from your membership.</p>
      <ul class="perks__list">
        <li>10% Discount on skin care products</li>
        <li>Share membership with your family</li>
        <li>Access to in-house monthly payment plans</li>
        <li>Exclusive monthly member savings</li>
      </ul>
    </div>
    <div class="perks__visual">
      <svg width="500" height="480" viewBox="0 0 500 480" aria-hidden="true" style="position:absolute;left:0;top:0">
        <circle cx="250" cy="230" r="215" fill="var(--amber)"/>
        <circle cx="245" cy="275" r="215" fill="var(--ink)"/>
        <circle cx="265" cy="258" r="208" fill="#ffffff"/>
      </svg>
      <div class="perks__photo" role="img" aria-label="Photo of a client in protective glasses receiving a laser treatment"></div>
    </div>
  </section>
</main>
</body>
</html>
```